Career Ad - Graphic Image to Attract New Team Members to our Company

We would like a career ad to be used for recruiting staff. This ad will be posted through our social media sites and may also be printed on post cards. Concept we like so far (however we are open to other creative ideas) is a photo in the background with printing on top. The color would be our brand color : blue. As for content, words like "We're Hiring" or "Come join our team" we'd also like to have reference to our website https://lindenvale.ca/about/careers and our email careers@lindenvale.ca Of course, our logo and company name, which is attached in the files
Target Market(s)
Professional
Requirements
Must have
- company logo
Nice to have
- visually apealling

```html
<!DOCTYPE html>
<html lang="en">
<head>
<meta charset="utf-8">
<title>Lindenvale Brokers — We're Hiring</title>
<link rel="stylesheet" href="https://fonts.googleapis.com/css2?family=Josefin+Sans:wght@200;300;700&family=Nunito:wght@900&display=swap">
<style>
  :root {
    --brand-navy: #1f2860;
    --pattern-navy: #1b2353;
    --ink-white: #ffffff;
  }
  * { margin: 0; padding: 0; box-sizing: border-box; }
  html, body {
    width: 960px;
    height: 1200px;
    overflow: hidden;
    background: var(--brand-navy);
  }
  .career-ad {
    position: relative;
    width: 960px;
    height: 1200px;
    overflow: hidden;
    color: var(--ink-white);
    font-family: "Josefin Sans", sans-serif;
  }
  .backdrop {
    position: absolute;
    inset: 0;
    background: radial-gradient(circle at 60% 40%, var(--brand-navy) 0%, var(--pattern-navy) 100%);
  }
  .brand {
    position: absolute;
    left: 78px;
    top: 122px;
    width: 266px;
    display: flex;
    align-items: center;
    justify-content: center;
    gap: 10px;
    font-family: "Josefin Sans", sans-serif;
    font-weight: 700;
    font-size: 24px;
    letter-spacing: 0.04em;
    text-transform: uppercase;
    white-space: nowrap;
  }
  .brand-mark {
    width: 14px;
    height: 14px;
    background: var(--ink-white);
    flex: none;
  }
  .headline {
    position: absolute;
    left: 68px;
    top: 322px;
    font-family: "Nunito", sans-serif;
    font-weight: 900;
    font-size: 182px;
    line-height: 166px;
    letter-spacing: 0.005em;
    text-transform: uppercase;
  }
  .tagline {
    position: absolute;
    left: 68px;
    top: 820px;
    font-weight: 200;
    font-size: 58px;
    letter-spacing: -0.01em;
    text-transform: uppercase;
    white-space: nowrap;
  }
  .contact {
    position: absolute;
    left: 68px;
    top: 1050px;
    font-weight: 300;
    font-size: 41px;
    line-height: 53px;
    white-space: nowrap;
  }
  .contact span { display: block; }
</style>
</head>
<body>
  <main class="career-ad">
    <div class="backdrop" role="img" aria-label="Navy background with a faint geometric line pattern"></div>

    <div class="brand">
      <span class="brand-mark"></span>
      <span class="brand-name">Lindenvale Brokers</span>
    </div>

    <h1 class="headline">We’re<br>Hiring</h1>

    <p class="tagline">Come join our team</p>

    <p class="contact">
      <span class="contact-url">https://lindenvale.ca/about/careers</span>
      <span class="contact-email">careers@lindenvale.ca</span>
    </p>
  </main>
</body>
</html>
```